political campaign lawn sign - Governor's Council in Massachuesetts

We are looking for a political lawn sign. We are running a campaign for Governor's Council in Massachusetts. This sign will be on the lawn of homes and businesses so people driving by will see it. It needs to be simple and bold. The last name is long so maybe it could say vote for Carl and then Malbonske will be big a bold on the next line??
We need it to say:
Vote for Carlton Malbonske
Governor's Council.

Target Market(s)

local residents

Industry/Entity Type

Politcal Campaign

Font styles to use
Sans Serif
Other font styles liked:
• not sure what font but a modern looking one such as Helvetica, Arial, Sans Seri, sharp sans..

Colors
0054AA
0677BA
7BADD7
CADEEF
E8F1F8
00AB8E
00BBA5
67D7C9
C6EFE9
E9F9F6
FFF300
FFF600
FEFA6F
FFFEC7
FFFEE8

Requirements
Must have
• My name written out with a Capital D and R but lower case for every other letter so its Carl Malbonske
Nice to have
• modern font , the Colors of the lawn sign should have Blue, Yellow and White something bold that will stand out
Should not have
• any maps of Massachusetts

```html
<!DOCTYPE html>
<html lang="en">
<head>
<meta charset="utf-8">
<title>Vote Carl Malbonske – Governor's Council Lawn Sign</title>
<link rel="stylesheet" href="https://fonts.googleapis.com/css2?family=Kaushan+Script&family=Montserrat:wght@700;800;900&display=swap">
<style>
  :root {
    --navy: #001B54;
    --yellow: #FFFF00;
    --white: #FFFFFF;
    --outline: #000000;
  }
  html, body {
    margin: 0;
    padding: 0;
    width: 1200px;
    height: 903px;
    overflow: hidden;
    background: var(--navy);
  }
  .lawn-sign {
    display: block;
    width: 1200px;
    height: 903px;
    background: var(--navy);
  }
  .frame-line {
    stroke: var(--white);
    stroke-width: 4.5;
    fill: none;
  }
  .vote-script {
    font-family: "Kaushan Script", cursive;
    font-size: 168px;
    fill: var(--white);
    stroke: var(--outline);
    stroke-width: 14px;
    stroke-linejoin: round;
    paint-order: stroke fill;
  }
  .first-name {
    font-family: "Montserrat", sans-serif;
    font-weight: 800;
    font-size: 440px;
    fill: var(--yellow);
    stroke: var(--outline);
    stroke-width: 15px;
    stroke-linejoin: miter;
    paint-order: stroke fill;
  }
  .last-name {
    font-family: "Montserrat", sans-serif;
    font-weight: 800;
    font-size: 136px;
    fill: var(--white);
  }
  .office {
    font-family: "Montserrat", sans-serif;
    font-weight: 800;
    font-size: 60px;
    fill: var(--yellow);
  }
</style>
</head>
<body>
<svg class="lawn-sign" viewBox="0 0 1200 903" xmlns="http://www.w3.org/2000/svg" role="img" aria-label="Vote Carl Malbonske, Governor's Council">
  <!-- frame -->
  <polyline class="frame-line" points="255,125 75,125 75,803"/>
  <polyline class="frame-line" points="634,125 1087,125 1087,150"/>
  <line class="frame-line" x1="1087" y1="383" x2="1087" y2="717"/>
  <line class="frame-line" x1="0" y1="831" x2="268" y2="814"/>
  <line class="frame-line" x1="932" y1="767" x2="1200" y2="746"/>

  <!-- headline -->
  <text class="vote-script" transform="translate(300 188) rotate(-8)" textLength="290" lengthAdjust="spacingAndGlyphs">Vote</text>
  <text class="first-name" transform="translate(140 588) rotate(-4.2)" textLength="975" lengthAdjust="spacingAndGlyphs">CARL</text>
  <text class="last-name" transform="translate(136 724) rotate(-4.2)" textLength="854" lengthAdjust="spacingAndGlyphs">MALBONSKE</text>
  <text class="office" transform="translate(293 828) rotate(-4.2)" textLength="620" lengthAdjust="spacingAndGlyphs">GOVERNER'S COUNCIL</text>
</svg>
</body>
</html>
```